A-Stand Directional Sign Design

Objective:
We need a professional graphic design for an A-Stand sign that will guide customers arriving in our parking lot to our office. The design should be visually clear, welcoming, and aligned with our brand identity.
REQUIREMENTS:
Two versions of the design:
- One with an arrow pointing left
- One with an arrow pointing right
(This allows us to place the A-Stand anywhere and flip the graphic as needed.)
DIMENSIONS:
- Viewable Area: 30" x 40"
BRAND ALIGNMENT:
- Colors, fonts, and overall style should match our website: www.glidecrest.com
- Clean, modern, and professional look consistent with our aviation/tourism brand
CONTENT:
- Clear directional arrow (left or right depending on version)
- Text: “Office Entrance” or similar concise wording (designers may propose alternatives if they improve clarity)
READABILITY:
- Bold, high-contrast design for visibility from a distance
- Simple layout that avoids clutter
DELIVERABLES:
- Final artwork in print-ready format (PDF preferred)
- Two versions: Arrow Left and Arrow Right
DESIGN GOAL:
Ensure customers can easily find our office upon arrival, while reinforcing glideCREST’s professional and welcoming brand image.
Target Market(s)
Tourism
Look and feel

```html
<!DOCTYPE html>
<html lang="en">
<head>
<meta charset="utf-8">
<title>glideCREST A-Stand Directional Signs</title>
<link rel="stylesheet" href="https://fonts.googleapis.com/css2?family=Michroma&display=swap">
<style>
  :root {
    --brand-blue: #3a70aa;
    --sign-black: #131313;
    --paper: #ffffff;
    --sky-warm-light: #f0b77a;
    --sky-warm-deep: #c98240;
    --sky-cool-light: #f1efec;
    --sky-cool-deep: #9d948c;
  }
  html, body {
    margin: 0;
    padding: 0;
    overflow: hidden;
    background: var(--paper);
  }
  .canvas {
    width: 1043px;
    height: 1200px;
    display: flex;
    align-items: center;
    justify-content: center;
    gap: 40px;
    background: var(--paper);
    overflow: hidden;
  }
  .sign {
    width: 440px;
    height: 584px;
    display: block;
  }
  .sign__field { fill: var(--sign-black); }
  .sign__band { fill: var(--brand-blue); }
  .sign__halo { fill: var(--paper); }
  .sign__swoosh {
    fill: none;
    stroke: var(--brand-blue);
    stroke-width: 9;
    stroke-linecap: round;
  }
  .sign__headline {
    font-family: "Michroma", sans-serif;
    fill: var(--paper);
    font-size: 62px;
  }
  .sign__arrow {
    stroke: var(--paper);
    stroke-width: 9;
    fill: none;
    stroke-linecap: round;
    stroke-linejoin: round;
  }
  .brand__dot { fill: var(--brand-blue); }
  .brand__name {
    font-family: "Michroma", sans-serif;
    fill: var(--brand-blue);
    font-size: 24px;
  }
</style>
</head>
<body>
<main class="canvas">

  <svg class="sign sign--left" viewBox="0 0 570 757" xmlns="http://www.w3.org/2000/svg" aria-label="Office entrance sign, arrow pointing left">
    <defs>
      <linearGradient id="warm-sky" x1="0" y1="0" x2="1" y2="1">
        <stop offset="0" stop-color="var(--sky-warm-light)"/>
        <stop offset="1" stop-color="var(--sky-warm-deep)"/>
      </linearGradient>
      <clipPath id="left-sheet"><rect width="570" height="757"/></clipPath>
    </defs>
    <g clip-path="url(#left-sheet)">
      <rect class="sign__field" width="570" height="757"/>
      <polygon class="sign__band" points="0,0 570,0 570,290 0,200"/>
      <ellipse class="sign__halo" cx="285" cy="213" rx="294" ry="200" transform="rotate(-20 285 213)"/>
      <ellipse class="sign__swoosh" cx="288" cy="213" rx="268" ry="178" transform="rotate(-20 288 213)" pathLength="100" stroke-dasharray="30 20"/>
      <ellipse cx="290" cy="212" rx="244" ry="154" transform="rotate(-20 290 212)" fill="url(#warm-sky)" role="img" aria-label="Photo of a helicopter flying through golden sunset clouds"/>
    </g>
    <path class="sign__arrow" d="M200 493 H54 M78 472 L54 493 L78 514"/>
    <text class="sign__headline" x="225" y="517" textLength="296" lengthAdjust="spacingAndGlyphs">OFFICE</text>
    <text class="sign__headline" x="50" y="604" textLength="471" lengthAdjust="spacingAndGlyphs">ENTRANCE</text>
    <g class="brand">
      <circle class="brand__dot" cx="152" cy="690" r="24"/>
      <text class="brand__name" x="190" y="699" textLength="300" lengthAdjust="spacingAndGlyphs">GLIDECREST.COM</text>
    </g>
  </svg>

  <svg class="sign sign--right" viewBox="0 0 570 757" xmlns="http://www.w3.org/2000/svg" aria-label="Office entrance sign, arrow pointing right">
    <defs>
      <linearGradient id="cool-sky" x1="0" y1="0" x2="0" y2="1">
        <stop offset="0" stop-color="var(--sky-cool-light)"/>
        <stop offset="1" stop-color="var(--sky-cool-deep)"/>
      </linearGradient>
      <clipPath id="right-sheet"><rect width="570" height="757"/></clipPath>
    </defs>
    <g clip-path="url(#right-sheet)">
      <rect class="sign__field" width="570" height="757"/>
      <polygon class="sign__band" points="0,0 570,0 570,200 0,290"/>
      <ellipse class="sign__halo" cx="285" cy="213" rx="294" ry="200" transform="rotate(20 285 213)"/>
      <ellipse class="sign__swoosh" cx="282" cy="213" rx="268" ry="178" transform="rotate(20 282 213)" pathLength="100" stroke-dasharray="30 20" stroke-dashoffset="50"/>
      <ellipse cx="280" cy="212" rx="244" ry="154" transform="rotate(20 280 212)" fill="url(#cool-sky)" role="img" aria-label="Photo of a helicopter parked on a wet landing pad under a cloudy sky"/>
    </g>
    <text class="sign__headline" x="48" y="517" textLength="296" lengthAdjust="spacingAndGlyphs">OFFICE</text>
    <path class="sign__arrow" d="M370 493 H516 M492 472 L516 493 L492 514"/>
    <text class="sign__headline" x="50" y="604" textLength="471" lengthAdjust="spacingAndGlyphs">ENTRANCE</text>
    <g class="brand">
      <circle class="brand__dot" cx="118" cy="686" r="24"/>
      <text class="brand__name" x="156" y="695" textLength="300" lengthAdjust="spacingAndGlyphs">GLIDECREST.COM</text>
    </g>
  </svg>

</main>
</body>
</html>
```